TriVex Business Card Design - double sided -plumbing local plumbing company

We have a Plumbing company where the design was create through Sketch Hive. We would now like a business card designed as well. We want it to be in the colour version of the logo.

Details below for the card.

Phone Number: 0438 615 247
Email: info@trivexplumbing.example.au
Website: https://trivexplumbing.example.au
We really want a sophisticated design that stand out from the other- informative and timeless.

Target Market(s)

local Canberra market

Industry/Entity Type

Plumbing, gas fitting, hot water

Contact Information for Business Card

Phone number, email, logo and "Supplying all your heating, cooling and hot water needs"

Requirements
Must have
• bust be colourful, must also be though about it being printed on a magnet. must Vex with the logo - I dont want the logo and information chucked onto a white canvas I would prefer it to be smooth and look purposeful

```html
<!DOCTYPE html>
<html lang="en">
<head>
<meta charset="utf-8">
<title>TriVex Business Card – Front and Back</title>
<link href="https://fonts.googleapis.com/css2?family=Arimo:ital,wght@0,400;0,700;1,700&display=swap" rel="stylesheet">
<style>
  :root {
    --orange: #f9ae42;
    --blue: #00a9e9;
    --white: #ffffff;
    --ink-bg: #e9eaec;
    --card-w: 700px;
    --card-h: 400px;
  }
  * { margin: 0; padding: 0; box-sizing: border-box; }
  html, body {
    width: 1200px; height: 874px; overflow: hidden;
    background: var(--ink-bg);
    font-family: "Arimo", Arial, sans-serif;
  }
  .sheet {
    width: 1200px; height: 874px;
    display: flex; flex-direction: column;
    align-items: center; justify-content: center; gap: 26px;
  }
  .card {
    position: relative;
    width: var(--card-w); height: var(--card-h);
    border-radius: 22px; overflow: hidden;
    box-shadow: 0 6px 18px rgba(0,0,0,.18);
  }

  /* Front */
  .card--front { background: var(--orange); color: var(--white); }
  .front__brand {
    position: absolute; left: 0; right: 0; top: 140px;
    display: flex; justify-content: center; align-items: center; gap: 14px;
  }
  .brand-name {
    font-weight: 700; font-size: 92px; letter-spacing: 4px; line-height: 1;
  }
  .brand-dot { width: 26px; height: 26px; border-radius: 50%; background: var(--white); }
  .front__tagline {
    position: absolute; left: 0; right: 0; top: 282px;
    text-align: center; font-size: 19px; letter-spacing: .2px;
  }
  .front__tagline strong { font-weight: 700; font-style: italic; }

  /* Back */
  .card--back { background: var(--white); }
  .back__brand {
    position: absolute; left: 34px; top: 40px;
    display: flex; align-items: center; gap: 12px;
  }
  .back__brand .brand-name { font-size: 70px; color: var(--blue); }
  .back__brand .brand-dot { width: 20px; height: 20px; background: var(--orange); }
  .back__wave { position: absolute; inset: 0; }
  .back__details {
    position: absolute; right: 34px; top: 222px;
    color: var(--white); text-align: right;
  }
  .person__name { font-size: 27px; font-weight: 700; letter-spacing: .5px; line-height: 31px; }
  .person__role { font-size: 17px; line-height: 20px; margin-top: 2px; margin-bottom: 12px; }
  .contact { list-style: none; }
  .contact__item {
    display: flex; justify-content: flex-end; align-items: center; gap: 12px;
    font-size: 18px; line-height: 26px;
  }
  .contact__icon { width: 16px; height: 16px; flex: none; }
</style>
</head>
<body>
<main class="sheet">

  <section class="card card--front" aria-label="Business card front">
    <div class="front__brand">
      <span class="brand-name">TRIVEX</span>
      <span class="brand-dot"></span>
    </div>
    <p class="front__tagline">Supplying all your <strong>heating, cooling</strong> and <strong>hot water</strong> needs</p>
  </section>

  <section class="card card--back" aria-label="Business card back">
    <svg class="back__wave" viewBox="0 0 700 400" preserveAspectRatio="none" aria-hidden="true">
      <path fill="var(--orange)" d="M0,220 C90,290 190,310 290,295 C400,278 500,122 700,112 L700,400 L0,400 Z"/>
      <path fill="var(--blue)" stroke="var(--white)" stroke-width="4" d="M0,238 C90,308 190,328 290,313 C400,296 500,140 700,130 L700,400 L0,400 Z"/>
    </svg>

    <div class="back__brand">
      <span class="brand-name">TRIVEX</span>
      <span class="brand-dot"></span>
    </div>

    <div class="back__details">
      <p class="person__name">MARK ELLISON</p>
      <p class="person__role">President</p>
      <ul class="contact">
        <li class="contact__item">0438 615 247
          <svg class="contact__icon" viewBox="0 0 16 16" aria-hidden="true"><path fill="#fff" d="M3.2 1l2.6 3-1.4 1.8c.8 1.8 2.2 3.2 4 4l1.8-1.4 3 2.6-1.6 2.2C6.8 13 3 9.2 1 4.6z"/></svg>
        </li>
        <li class="contact__item">info@trivexplumbing.example.au
          <svg class="contact__icon" viewBox="0 0 16 16" aria-hidden="true"><rect x="1" y="3" width="14" height="10" rx="1" fill="#fff"/><path d="M1.5 3.5L8 9l6.5-5.5" fill="none" stroke="var(--blue)" stroke-width="1.3"/></svg>
        </li>
        <li class="contact__item">www.trivexplumbing.example.au
          <svg class="contact__icon" viewBox="0 0 16 16" aria-hidden="true"><circle cx="8" cy="8" r="7" fill="#fff"/><path d="M1 8h14M8 1c-3 3.5-3 10.5 0 14M8 1c3 3.5 3 10.5 0 14" fill="none" stroke="var(--blue)" stroke-width="1.1"/></svg>
        </li>
      </ul>
    </div>
  </section>

</main>
</body>
</html>
```